Post Lockdown Ortho Special

We are running a special for (Ortho) Braces/Clear Aligner (Quorventa), till July 31st 2020. Up to $2,000 off with free Consultation and Xrays.

We need a ad to run in different formats.

Maybe something with: what better time to get braces when you have to wear a mask all the time.

Trying to rebuild our business and get people in for free consultations.

```html
<!DOCTYPE html>
<html lang="en">
<head>
<meta charset="utf-8">
<title>Ridgeline Family Dentistry – Post Lockdown Ortho Special</title>
<link rel="stylesheet" href="https://fonts.googleapis.com/css2?family=Cinzel:wght@700&family=Libre+Baskerville:wght@400;700&family=Nunito+Sans:wght@300;400&family=Oswald:wght@300;600&display=swap">
<style>
  :root {
    --white: #ffffff;
    --purple-bright: #a22dd0;
    --purple-mid: #8a16c2;
    --purple-deep: #4d216f;
    --purple-dark: #3c1558;
    --brand-purple: #5a3a8c;
    --offer-purple: #8d14c8;
    --photo-light: #ece8ef;
    --photo-lilac: #b9a2d8;
  }
  * { box-sizing: border-box; margin: 0; padding: 0; }
  html, body { width: 1200px; height: 817px; overflow: hidden; background: var(--white); }
  .ad { position: relative; width: 1200px; height: 817px; overflow: hidden; background: var(--white); }
  .ad-shapes { position: absolute; inset: 0; width: 1200px; height: 817px; }

  .brand { position: absolute; left: 40px; top: 62px; display: flex; align-items: center; gap: 22px; }
  .brand-dot { width: 74px; height: 74px; border-radius: 50%; background: var(--photo-lilac); }
  .brand-text { color: var(--brand-purple); font-family: "Cinzel", serif; font-weight: 700; }
  .brand-name { font-size: 36px; line-height: 1; letter-spacing: 1px; }
  .brand-sub { font-size: 12.5px; letter-spacing: 6.6px; margin-top: 6px; padding-bottom: 6px; border-bottom: 1px solid var(--brand-purple); }
  .brand-doctor { font-size: 11px; letter-spacing: 1.4px; margin-top: 6px; text-align: center; }

  .pitch { position: absolute; left: 62px; top: 296px; color: var(--white); }
  .pitch-lead { font-family: "Nunito Sans", sans-serif; font-weight: 300; font-size: 22px; letter-spacing: .3px; }
  .pitch-title { font-family: "Libre Baskerville", serif; font-weight: 700; font-size: 50px; line-height: 1; margin-top: 6px; letter-spacing: .5px; }
  .pitch-sub { font-family: "Libre Baskerville", serif; font-weight: 400; font-size: 19.5px; line-height: 27px; margin-top: 10px; letter-spacing: .4px; }
  .pitch-body { font-family: "Nunito Sans", sans-serif; font-weight: 300; font-size: 25px; line-height: 39px; margin-top: 26px; }

  .offer-date { position: absolute; left: 86px; top: 643px; width: 407px; height: 54px; background: var(--white);
    display: flex; align-items: center; justify-content: center;
    font-family: "Nunito Sans", sans-serif; font-weight: 300; font-size: 31px; color: var(--offer-purple); }

  .deal { position: absolute; left: 465px; top: 76px; width: 284px; height: 284px; border-radius: 50%;
    display: flex; flex-direction: column; align-items: center; justify-content: center;
    color: var(--white); font-family: "Nunito Sans", sans-serif; font-weight: 300; text-align: center; padding-top: 4px; }
  .deal-upto { font-size: 31px; line-height: 1; }
  .deal-amount { display: flex; align-items: center; margin: 4px 0 2px 12px; }
  .deal-price { font-family: "Oswald", sans-serif; font-weight: 600; font-size: 66px; line-height: 1; letter-spacing: -1px; }
  .deal-off { font-family: "Oswald", sans-serif; font-weight: 300; font-size: 20px; writing-mode: vertical-rl; transform: rotate(180deg); letter-spacing: 1px; margin-left: 3px; }
  .deal-terms { font-size: 31px; line-height: 35px; }
</style>
</head>
<body>
<main class="ad">
  <svg class="ad-shapes" viewBox="0 0 1200 817" xmlns="http://www.w3.org/2000/svg">
    <defs>
      <linearGradient id="panelFill" x1="0" y1="0" x2="0.6" y2="1">
        <stop offset="0" stop-color="var(--purple-bright)"/>
        <stop offset="0.55" stop-color="#6a2590"/>
        <stop offset="1" stop-color="var(--purple-dark)"/>
      </linearGradient>
      <linearGradient id="ringFill" x1="0" y1="0" x2="0" y2="1">
        <stop offset="0" stop-color="var(--purple-mid)"/>
        <stop offset="1" stop-color="var(--purple-deep)"/>
      </linearGradient>
      <linearGradient id="badgeFill" x1="0" y1="0" x2="0.4" y2="1">
        <stop offset="0" stop-color="#9c16cf"/>
        <stop offset="1" stop-color="#532a7c"/>
      </linearGradient>
      <radialGradient id="photoFill" cx="0.6" cy="0.45" r="0.7">
        <stop offset="0" stop-color="var(--photo-lilac)"/>
        <stop offset="1" stop-color="var(--photo-light)"/>
      </radialGradient>
    </defs>

    <path class="purple-panel" fill="url(#panelFill)"
      d="M0,277 C160,205 360,168 560,140 L560,0 L1000,0 C1000,60 975,90 930,100 C890,110 860,118 830,130
         L872,672 C940,690 995,725 1000,817 L0,817 Z"/>

    <circle class="photo-halo" cx="872" cy="400" r="272" fill="var(--white)"/>
    <circle class="photo-ring" cx="872" cy="400" r="231" fill="url(#ringFill)"/>
    <circle class="photo-window" cx="872" cy="400" r="207" fill="url(#photoFill)"
      role="img" aria-label="Photo of a gloved hand holding a dental X-ray film"/>

    <circle class="deal-halo" cx="607" cy="218" r="163" fill="var(--white)"/>
    <circle class="deal-disc" cx="607" cy="218" r="142" fill="url(#badgeFill)"/>
  </svg>

  <header class="brand">
    <div class="brand-dot"></div>
    <div class="brand-text">
      <div class="brand-name">RIDGELINE</div>
      <div class="brand-sub">FAMILY DENTISTRY</div>
      <div class="brand-doctor">DR MAREN HOLLOWAY</div>
    </div>
  </header>

  <section class="pitch">
    <p class="pitch-lead">WHAT BETTER TIME TO</p>
    <h1 class="pitch-title">GET BRACES</h1>
    <p class="pitch-sub">WHEN YOU HAVE TO WEAR A MASK<br>ALL THE TIME</p>
    <p class="pitch-body">Trying to rebuild our business and<br>get people in for free consultations.</p>
  </section>

  <p class="offer-date">Offer: till July 31st 2020</p>

  <aside class="deal">
    <span class="deal-upto">Up to</span>
    <span class="deal-amount"><span class="deal-price">$2,000</span><span class="deal-off">OFF</span></span>
    <span class="deal-terms">with free<br>Consultation<br>and Xrays</span>
  </aside>
</main>
</body>
</html>
```